Business Card Design

Professional solutions in (servers, security, networks, programming)

Industry/Entity Type

Business

Contact Information for Business Card

Nadim Fouzan
Internet services and network solutions
TDK - GLPW - GLPT
netdesk@kavo-lin.com / 05291473806
www.kavo-lin.com

```html
<!DOCTYPE html>
<html lang="en">
<head>
<meta charset="utf-8">
<title>Nadim Fouzan — Business Card</title>
<link rel="stylesheet" href="https://fonts.googleapis.com/css2?family=Cormorant+SC:wght@500;600;700&display=swap">
<style>
  :root {
    --card-bg: #ffffff;
    --ink-blue: #124a7c;
    --ink-blue-soft: #1f4c7e;
    --rule-gold: #d6aa55;
  }
  html, body {
    margin: 0;
    padding: 0;
    width: 1200px;
    height: 702px;
    overflow: hidden;
    background: var(--card-bg);
  }
  .card {
    position: relative;
    width: 1200px;
    height: 702px;
    background: var(--card-bg);
    font-family: "Cormorant SC", "Times New Roman", serif;
    color: var(--ink-blue-soft);
  }
  .card__line {
    position: absolute;
    left: 0;
    width: 100%;
    margin: 0;
    text-align: center;
    white-space: nowrap;
    line-height: 1;
  }
  .card__name {
    top: 122px;
    font-size: 92px;
    font-weight: 700;
    color: var(--ink-blue);
    letter-spacing: 1px;
  }
  .card__rule {
    position: absolute;
    left: 341px;
    top: 241px;
    width: 528px;
    height: 3px;
    background: var(--rule-gold);
  }
  .card__tagline,
  .card__credentials,
  .card__contact,
  .card__website {
    font-size: 31px;
    font-weight: 600;
    letter-spacing: 0.5px;
  }
  .card__tagline { top: 298px; }
  .card__credentials { top: 380px; }
  .card__contact { top: 462px; }
  .card__website { top: 544px; }
</style>
</head>
<body>
  <main class="card">
    <h1 class="card__line card__name">Nadim Fouzan</h1>
    <div class="card__rule" aria-hidden="true"></div>
    <p class="card__line card__tagline">internet services and network solutions</p>
    <p class="card__line card__credentials">tdk - glpw - glpt</p>
    <p class="card__line card__contact">netdesk@kavo-lin.com / 05291473806</p>
    <p class="card__line card__website">www.kavo-lin.com</p>
  </main>
</body>
</html>
```